Mavro Scrub - Contact/Landing Page

I need a landing page which will essentially be the page that customers will go to from the 'website' link on GMB listing. It will provide a short overview of services which need to be selectable. a little further down can capture some contact details followed by a large Submit Now button etc...

I have some icon/logo's that can be utilised at the bottom of the page as industry type references.

Target Market(s)

End of Lease Cleaning Services

Industry/Entity Type

Cleaning Service

Colors

Designer to choose colors to be used in the design.

Requirements
Must have
• As per description
Should not have
• Colours to match my website mavroscrub.com.au

```html
<!DOCTYPE html>
<html lang="en">
<head>
<meta charset="utf-8">
<title>Mavro Scrub – End of Lease Services</title>
<link href="https://fonts.googleapis.com/css2?family=Mulish:ital,wght@0,400;0,600;0,700;0,800;1,800&display=swap" rel="stylesheet">
<style>
:root{
  --blue:#27a3e0;
  --blue-deep:#1b8fd0;
  --hero-a:#6f8fc4;
  --hero-b:#a9bfe0;
  --ink:#2a2a2a;
  --text:#333;
  --dark-btn:#3a3a3a;
  --footer-a:#4a4a4a;
  --footer-b:#2d2d2d;
  --line:#d9dde2;
  --white:#fff;
}
*{box-sizing:border-box;margin:0;padding:0}
html,body{width:1200px;height:2385px;overflow:hidden}
body{position:relative;font-family:"Mulish",sans-serif;color:var(--text);background:var(--white)}
.abs{position:absolute}

.hero{left:0;top:0;width:1200px;height:545px;
  background:
    radial-gradient(ellipse 220px 300px at 130px 230px,rgba(214,226,244,.75),rgba(214,226,244,0)),
    radial-gradient(ellipse 200px 260px at 1130px 230px,rgba(214,226,244,.6),rgba(214,226,244,0)),
    radial-gradient(ellipse 520px 120px at 600px 470px,rgba(70,100,160,.55),rgba(70,100,160,0)),
    linear-gradient(180deg,#8fa9d4 0%,#a2b8de 45%,#7f98c8 78%,#6f89bb 100%)}
.brand-mark{left:562px;top:78px;width:76px;height:76px;border-radius:50%;background:var(--white);opacity:.92}
.brand{left:0;top:178px;width:1200px;text-align:center;font-weight:800;font-size:84px;line-height:1;color:var(--blue-deep);letter-spacing:1px}
.brand-rule{left:516px;top:375px;width:218px;height:3px;background:#1d2b4a}
.hero-title{left:0;top:390px;width:1235px;text-align:center;font-weight:800;font-style:italic;font-size:37px;color:var(--white)}

.section-title{width:1200px;left:0;text-align:center;font-weight:800;font-style:italic;font-size:38px;color:var(--ink)}
.services-title{top:598px;left:17px}
.card-img{top:669px;width:257px;height:271px}
.card-img.property{left:189px;background:
  radial-gradient(ellipse 90px 120px at 50px 190px,rgba(140,196,60,.85),rgba(140,196,60,0)),
  linear-gradient(180deg,#ece8e2 0%,#ddd6cc 50%,#c49a6c 78%,#a87848 100%)}
.card-img.carpet{left:471px;background:
  radial-gradient(ellipse 90px 110px at 130px 90px,rgba(90,92,100,.6),rgba(90,92,100,0)),
  linear-gradient(180deg,#eef0f3 0%,#d4d6da 38%,#8f929a 62%,#767982 100%)}
.card-img.pest{left:754px;background:
  radial-gradient(ellipse 110px 80px at 170px 60px,rgba(236,226,214,.9),rgba(236,226,214,0)),
  linear-gradient(170deg,#e6dccf 0%,#d2c1ad 45%,#b9a38c 70%,#d8ccbf 100%)}
.card-name{top:955px;font-size:24px;font-weight:600;color:var(--ink)}
.card-desc{top:994px;width:250px;font-size:15.5px;line-height:25px;color:var(--text)}
.btn-select{top:1078px;width:120px;height:42px;display:flex;align-items:center;justify-content:center;gap:14px;font-size:18px;color:var(--white);background:var(--dark-btn)}
.btn-select.active{background:var(--blue)}
.btn-select .box{width:21px;height:21px;border:2px solid var(--white)}

.contact-band{left:0;top:1198px;width:1200px;height:479px;background:linear-gradient(90deg,#eef2f5 0%,#f6f8fa 55%,#fbfcfd 100%)}
.contact-photo{left:0;top:1198px;width:600px;height:479px;background:
  radial-gradient(ellipse 170px 220px at 300px 330px,rgba(62,112,182,.9),rgba(62,112,182,0)),
  radial-gradient(ellipse 120px 160px at 500px 180px,rgba(255,255,255,.9),rgba(255,255,255,0)),
  radial-gradient(ellipse 140px 200px at 90px 230px,rgba(150,185,130,.55),rgba(150,185,130,0)),
  linear-gradient(90deg,#e3ebe6 0%,#e9eef2 60%,rgba(246,248,250,0) 100%)}
.field{left:599px;width:353px;height:42px;background:var(--white);border:1px solid var(--line);border-radius:2px;display:flex;align-items:center;font-size:11.5px;color:#555}
.field .ico{width:37px;height:24px;display:flex;align-items:center;justify-content:center;border-right:1px solid var(--line);margin-right:12px}
.submit{left:599px;top:1560px;width:113px;height:36px;background:var(--blue);color:var(--white);font-weight:700;font-size:19px;display:flex;align-items:center;justify-content:center;border-radius:2px}

.accred-title{top:1745px;left:0}
.badge{width:254px;height:139px;background:var(--white);box-shadow:0 0 6px rgba(0,0,0,.12);display:flex;flex-direction:column;align-items:center;justify-content:center;gap:8px}
.badge-mark{border-radius:8px}
.licence{font-size:12px;color:var(--ink)}

.footer{left:0;top:2188px;width:1200px;height:156px;background:linear-gradient(180deg,var(--footer-a),var(--footer-b))}
.f-icon{width:52px;height:52px;border-radius:50%;background:var(--blue);display:flex;align-items:center;justify-content:center}
.f-label{font-size:14.5px;color:var(--white)}
.f-text{font-size:13px;line-height:21px;color:#e6e6e6}
.copyright{left:0;top:2344px;width:1200px;height:41px;background:var(--blue);color:var(--white);font-size:13px;display:flex;align-items:center;justify-content:center}
.copyright b{font-weight:700;margin:0 3px}
</style>
</head>
<body>

<div class="abs hero" role="img" aria-label="Bright living room interior with sofa, windows and pendant lamps, tinted blue"></div>
<div class="abs brand-mark"></div>
<div class="abs brand">Mavro Scrub</div>
<div class="abs brand-rule"></div>
<h1 class="abs hero-title">End of Lease Services</h1>

<h2 class="abs section-title services-title">Select Your Service</h2>

<div class="abs card-img property" role="img" aria-label="Mop and bucket of cleaning supplies on a wooden floor"></div>
<div class="abs card-name" style="left:190px">Property Cleaning</div>
<p class="abs card-desc" style="left:192px;width:235px">All interior Cleaning carried out to property&nbsp; Management requirements</p>
<div class="abs btn-select active" style="left:193px">Select
  <svg width="22" height="22" viewBox="0 0 22 22"><rect x="1" y="3" width="18" height="18" fill="none" stroke="#fff" stroke-width="2"/><path d="M5 11l5 5 11-14" fill="none" stroke="#fff" stroke-width="3"/></svg>
</div>

<div class="abs card-img carpet" role="img" aria-label="Carpet steam cleaning wand on grey carpet"></div>
<div class="abs card-name" style="left:472px">Carpet Cleaning</div>
<p class="abs card-desc" style="left:472px">Carpet Steam Cleaning to<br>Australian Standard<br>AS 3733:1995</p>
<div class="abs btn-select" style="left:472px">Select <span class="box"></span></div>

<div class="abs card-img pest" role="img" aria-label="Technician spraying pest treatment along a skirting board"></div>
<div class="abs card-name" style="left:761px">Pest Control</div>
<p class="abs card-desc" style="left:761px">Mandatory Requirement&nbsp; for pets on premises</p>
<div class="abs btn-select" style="left:761px">Select <span class="box"></span></div>

<div class="abs contact-band"></div>
<div class="abs contact-photo" role="img" aria-label="Smiling cleaner holding a mop and a caddy of cleaning products"></div>

<div class="abs field" style="top:1280px"><span class="ico"><svg width="11" height="11" viewBox="0 0 12 12" fill="#27a3e0"><circle cx="6" cy="3.2" r="3"/><path d="M0 12c0-4 2.5-5.5 6-5.5S12 8 12 12z"/></svg></span>First Name*</div>
<div class="abs field" style="top:1335px"><span class="ico"><svg width="11" height="11" viewBox="0 0 12 12" fill="#27a3e0"><circle cx="6" cy="3.2" r="3"/><path d="M0 12c0-4 2.5-5.5 6-5.5S12 8 12 12z"/></svg></span>Last Name*</div>
<div class="abs field" style="top:1390px"><span class="ico"><svg width="11" height="11" viewBox="0 0 12 12" fill="#27a3e0"><path d="M2.5 0.5l2 2.5-1.2 1.5c.8 1.7 2.2 3.1 3.8 3.9l1.5-1.2 2.5 2-1.3 2.3C5 11 1 7 .3 1.8z"/></svg></span>Your Phone*</div>
<div class="abs field" style="top:1445px"><span class="ico"><svg width="12" height="9" viewBox="0 0 12 9" fill="#27a3e0"><path d="M0 0h12v1.5L6 5 0 1.5z"/><path d="M0 3l6 3.5L12 3v6H0z"/></svg></span>Your Email*</div>
<div class="abs field" style="top:1500px"><span class="ico"><svg width="14" height="18" viewBox="0 0 14 18"><path d="M7 17s6-6.5 6-10.5a6 6 0 0 0-12 0C1 10.5 7 17 7 17z" fill="none" stroke="#27a3e0" stroke-width="1.3"/><circle cx="7" cy="6.5" r="2.2" fill="none" stroke="#27a3e0" stroke-width="1.3"/></svg></span>Suburb</div>
<div class="abs submit">Submit</div>

<h2 class="abs section-title accred-title">Our Accreditations</h2>

<div class="abs badge" style="left:188px;top:1800px"><div class="badge-mark" style="width:218px;height:90px;background:linear-gradient(90deg,#e4ecef 0%,#e4ecef 40%,#151515 40%,#151515 100%);border:1px solid #222"></div></div>
<div class="abs badge" style="left:473px;top:1800px"><div class="badge-mark" style="width:230px;height:62px;background:linear-gradient(90deg,#dfe3f1 0%,#e9d6da 100%)"></div></div>
<div class="abs badge" style="left:758px;top:1800px"><div class="badge-mark" style="width:170px;height:110px;background:linear-gradient(90deg,#e0e4f0 0%,#e0e4f0 100%)"></div></div>
<div class="abs badge" style="left:331px;top:1977px"><div class="badge-mark" style="width:232px;height:70px;background:#7bbf3a;border-radius:0"></div></div>
<div class="abs badge" style="left:616px;top:1977px"><div class="badge-mark" style="width:218px;height:76px;background:#e2e6ee"></div><div class="licence">Pest Licence : 5014862</div></div>

<div class="abs footer"></div>
<div class="abs f-icon" style="left:195px;top:2239px"><svg width="24" height="24" viewBox="0 0 24 24"><path d="M6 2l4 5-2.4 2.4c1.5 3.3 3.8 5.6 7 7L17 14l5 4-2.5 4C10 21 3 14 2 4.5z" fill="none" stroke="#fff" stroke-width="1.5"/></svg></div>
<div class="abs f-label" style="left:260px;top:2245px">Phone</div>
<div class="abs f-text" style="left:260px;top:2268px">0400 318 274</div>

<div class="abs f-icon" style="left:414px;top:2239px"><svg width="20" height="26" viewBox="0 0 20 26"><path d="M10 24s8-9 8-14a8 8 0 0 0-16 0c0 5 8 14 8 14z" fill="none" stroke="#fff" stroke-width="1.6"/><circle cx="10" cy="10" r="3" fill="none" stroke="#fff" stroke-width="1.6"/></svg></div>
<div class="abs f-text" style="left:475px;top:2233px">Areas We Serve<br>Parramatta, Baulkham Hills, Mount Druitt,<br>Seven Hills, Blacktown, Penrith,Hills District.</div>

<div class="abs f-icon" style="left:793px;top:2239px"><svg width="26" height="22" viewBox="0 0 26 22"><path d="M2 8l11-6 11 6v12H2z M2 8l11 7 11-7" fill="none" stroke="#fff" stroke-width="1.5"/></svg></div>
<div class="abs f-label" style="left:857px;top:2245px">Email</div>
<div class="abs f-text" style="left:857px;top:2266px">info@mavroscrub.com.au</div>

<div class="abs copyright">Copyright © 2021 <b>Mavro Scrub.</b> All Rights Reserved.</div>

</body>
</html>
```